Homepage design competition to choose a designer for $1500 full website for a Small Animal Veterinar

We are running a homepage design competition to choose a designer who will later code an entire website. Please note, this competition is only for the front page design. There will be an additional payment of $1500 (Australian $AUD) for the complete website design including coding payment.

Front Page: First we need a front page design for our companion animal veterinary hospital. I will use the frontpage design competition to choose a designer for the full website.
Marlow Vet Clinic is a companion animal veterinary hospital in Singleton NSW. We provide veterinary medical and surgical treatment for dogs, cats, rabbits, birds and reptiles. Mostly dogs and cats.
Our reception is a 120 year old church and the hospital is 6 years old and custom built.
I want the site to be amazing. The sort of thing that could win prizes. The front page should be simple, fun and engaging whilst maintaining a strong sense of professionalism. Simple and elegant visual effects with subtle movement. The winning design will show originality.
Our main demographic is women aged 25 to 44 years old. We are a coal mining town. Most of our money comes from coal miners wives.
The front page must display our phone number and link to our facebook page. Otherwise the front page can have anything. The front page should impress new clients and reassure existing clients.
We pride ourselves on following up everything and caring for pets and their people their entire life. Please see our existing (horrible) website for more details about our business. http://www.marlowvetclinic.example/
Incorporate only amazing things from the old website. I hate the old website, so there is probably not much to use. We need something new and amazing.
Fully responsive design.

Characters: We have a logo and animal characters to incorporate into the design. These characters will be used throughout our email and facebook advertising. If they could be used with some movement and sound effects, that would be cool, but nothing too childish or silly.

Live site: please include links to live demo sites if possible.
Please include links to your other work.

Full Website: The successful designer of the frontpage must be able to demonstrate the ability produce a full website. The full website designer will be commissioned after the front page is chosen. We have budgeted for a full website of $1500.
I need to be able to add new articles to the website that will link from email newsletters and facebook, so the full website will need to be something I can modify or add to.
I have a working knowledge of Joomla, Wordpress and html.
The full website will have map, history of the hospital, history of the chapel, links to local services, pet care advice, memorials.
Ideally the winning designer will be able to integrate appointments available with our existing veterinary management software.
Fully responsive design.

Here are some websites that I like:
https://drbexley.example.au/
http://quincepepper.example/
http://www.xn--dorotawelnicka-abc12k.example/
https://www.zov.example.au/
https://www.frisko.example.au/
https://topmowers.example.au/
https://www.redgatecider.example/

Target Market(s)

Women aged 25 to 44 years

Industry/Entity Type

Veterinary

Number of Pages Required

1 page

Font styles to use
Serif
Sans Serif

Requirements
Must have
• Phone number
• Facebook Link https://www.facebook.com/marlow.vetclinic?v=wall
• Simplicity
• Originality
• Animal characters-images attached
Nice to have
• Images
• Clean
• Link to live site.
• Links to your other work.
• Demonstrate ability to integrate appointment booking with our veterinary software
Should not have
• Heaps of words
• Complexity

```html
<!DOCTYPE html>
<html lang="en">
<head>
<meta charset="utf-8">
<title>Marlow Vet Clinic – Navigation</title>
<link href="https://fonts.googleapis.com/css2?family=EB+Garamond:wght@400&family=Jost:ital,wght@0,400;0,500;1,400&display=swap" rel="stylesheet">
<style>
  :root {
    --bg: #f6fcf5;
    --ink: #111111;
    --muted: #8a8a8a;
    --menu: #a88a72;
    --hill-light: #cdf0c6;
    --hill-mid: #b4e8ab;
    --cat: #e8a779;
    --dog: #9c8170;
  }
  * { margin: 0; padding: 0; box-sizing: border-box; }
  html, body { width: 1200px; height: 576px; overflow: hidden; }
  body {
    position: relative;
    background: var(--bg);
    font-family: "Jost", sans-serif;
    color: var(--ink);
  }
  a { color: inherit; text-decoration: none; }

  .nav-label {
    position: absolute;
    left: 286px; top: 34px;
    font-size: 13px; font-weight: 500;
    letter-spacing: 0.3px;
    color: var(--muted);
    display: flex; align-items: center; gap: 6px;
    white-space: nowrap;
  }
  .nav-label svg { width: 14px; height: 12px; }

  .emergency {
    position: absolute;
    left: 805px; top: 20px;
    width: 322px;
    padding-bottom: 3px;
    border-bottom: 2px solid var(--ink);
    display: flex; align-items: baseline; justify-content: space-between;
    white-space: nowrap;
  }
  .emergency-label { font-size: 15px; font-style: italic; letter-spacing: 0.2px; }
  .emergency-number { font-size: 29px; font-weight: 500; letter-spacing: 0.3px; line-height: 1.1; }

  .menu {
    position: absolute;
    left: 482px; top: 117px;
    list-style: none;
  }
  .menu-item {
    display: flex; align-items: center;
    height: 64.5px;
    white-space: nowrap;
  }
  .menu-icon { width: 26px; height: 26px; margin-right: 22px; flex: none; }
  .menu-link {
    font-family: "EB Garamond", serif;
    font-size: 39px;
    color: var(--menu);
    letter-spacing: 0;
  }
  .menu-link--home { margin-left: 8px; }

  .close-toggle {
    position: absolute;
    left: 14px; top: 328px;
    display: flex; align-items: flex-start; gap: 4px;
  }
  .close-label {
    writing-mode: vertical-rl;
    transform: rotate(180deg);
    font-size: 12px; font-weight: 500; letter-spacing: 0.8px;
  }
  .close-toggle svg { width: 14px; height: 12px; margin-top: 20px; }

  .hills { position: absolute; left: 0; bottom: 0; width: 1200px; height: 110px; }

  .mascots {
    position: absolute;
    left: 722px; top: 340px;
    width: 318px; height: 236px;
    border-radius: 120px 120px 0 0;
    background: linear-gradient(90deg, var(--cat) 0%, var(--cat) 52%, var(--dog) 58%, var(--dog) 100%);
    opacity: 0.85;
  }
</style>
</head>
<body>

  <div class="nav-label">NAVIGATIONS
    <svg viewBox="0 0 14 12" fill="none" stroke="currentColor" stroke-width="1.5"><path d="M0 6h12M7 1l5 5-5 5"/></svg>
  </div>

  <a class="emergency" href="tel:0400555017">
    <span class="emergency-label">FOR EMERGENCY</span>
    <span class="emergency-number">0400 555 017</span>
  </a>

  <ul class="menu">
    <li class="menu-item">
      <svg class="menu-icon" viewBox="0 0 26 26" fill="var(--ink)"><path d="M3 10h14v15H3z"/><circle cx="10" cy="6" r="5"/><path d="M18 14h6v11h-6z"/><path d="M9 3h2v6H9zM7 5h6v2H7z" fill="#fff"/><path d="M6 14h2v2H6zM12 14h2v2h-2zM6 19h2v2H6zM12 19h2v2h-2zM20 16h2v2h-2zM20 20h2v2h-2z" fill="#fff"/></svg>
      <a class="menu-link menu-link--home" href="#home">HOME</a>
    </li>
    <li class="menu-item">
      <svg class="menu-icon" viewBox="0 0 26 26" fill="none" stroke="var(--ink)" stroke-width="2.4"><circle cx="13" cy="14" r="10"/><path d="M8 19l10-10"/><path d="M13 1v4M11 3h4" stroke-width="1.8"/></svg>
      <a class="menu-link" href="#services">SERVICES</a>
    </li>
    <li class="menu-item">
      <svg class="menu-icon" viewBox="0 0 26 26" fill="var(--ink)"><circle cx="13" cy="8" r="4"/><circle cx="5" cy="10" r="3"/><circle cx="21" cy="10" r="3"/><path d="M6 21c0-5 3-8 7-8s7 3 7 8z"/><path d="M0 20c0-4 2-6 5-6 1 0 2 .3 2.5 1C6 16.5 5 18 5 20z"/><path d="M26 20c0-4-2-6-5-6-1 0-2 .3-2.5 1 1.5 1.5 2.5 3 2.5 5z"/></svg>
      <a class="menu-link" href="#team">TEAM</a>
    </li>
    <li class="menu-item">
      <svg class="menu-icon" viewBox="0 0 24 24" fill="var(--ink)"><path d="M6.6 10.8a15.1 15.1 0 0 0 6.6 6.6l2.2-2.2a1 1 0 0 1 1-.25 11.4 11.4 0 0 0 3.6.6 1 1 0 0 1 1 1V20a1 1 0 0 1-1 1A17 17 0 0 1 3 4a1 1 0 0 1 1-1h3.5a1 1 0 0 1 1 1c0 1.250.2 2.450.6 3.6a1 1 0 0 1-.25 1z"/></svg>
      <a class="menu-link" href="#contact">CONTACT</a>
    </li>
    <li class="menu-item">
      <svg class="menu-icon" viewBox="0 0 26 26" fill="var(--ink)"><path d="M13 1L1 7v2h24V7z"/><path d="M3 10h3v10H3zM9 10h3v10H9zM14 10h3v10h-3zM20 10h3v10h-3z"/><path d="M1 21h24v2H1zM0 24h26v2H0z"/></svg>
      <a class="menu-link" href="#history">HISTORY</a>
    </li>
  </ul>

  <a class="close-toggle" href="#">
    <span class="close-label">CLOSE</span>
    <svg viewBox="0 0 14 12" fill="none" stroke="currentColor" stroke-width="1.5"><path d="M14 6H2M7 1L2 6l5 5"/></svg>
  </a>

  <svg class="hills" viewBox="0 0 1200 110" role="img" aria-label="Soft green low-poly hills along the bottom edge" preserveAspectRatio="none">
    <defs>
      <linearGradient id="hillFill" x1="0" y1="0" x2="0" y2="1">
        <stop offset="0" stop-color="var(--hill-light)"/>
        <stop offset="1" stop-color="var(--hill-mid)"/>
      </linearGradient>
    </defs>
    <path d="M0 78 L60 55 L120 34 L170 50 L240 25 L330 2 L450 14 L540 52 L620 42 L700 60 L760 70 L900 58 L1000 72 L1100 80 L1200 86 L1200 110 L0 110 Z" fill="url(#hillFill)"/>
  </svg>

  <div class="mascots" role="img" aria-label="Illustration of the clinic's cat and dog characters sitting side by side"></div>

</body>
</html>
```